Business Card Design for Engineering Firm

Need a business card design for small mechanical and plumbing engineering form based in Utah. Design should be customizable for all employees.

```html
<!DOCTYPE html>
<html lang="en">
<head>
<meta charset="utf-8">
<title>Halvorsen Engineering – Business Card</title>
<link rel="stylesheet" href="https://fonts.googleapis.com/css2?family=Montserrat:wght@300;400;600;800&display=swap">
<style>
  :root {
    --stage: #1c1c1e;
    --card-light: #ffffff;
    --card-dark: #2a2a2c;
    --pattern-a: #3a3a3d;
    --pattern-b: #202022;
    --brand-red: #861812;
    --ink: #2d2d2f;
    --ink-soft: #5a5a5c;
    --line-light: #e8e8e8;
  }
  * { margin: 0; padding: 0; box-sizing: border-box; }
  html, body {
    width: 1200px;
    height: 900px;
    overflow: hidden;
    background: var(--stage);
    font-family: "Montserrat", sans-serif;
  }
  .canvas {
    position: relative;
    width: 1200px;
    height: 900px;
  }
  .card {
    position: absolute;
    left: 260px;
    width: 680px;
    height: 388px;
    border-radius: 26px;
    overflow: hidden;
    box-shadow: 0 18px 40px rgba(0,0,0,0.45);
  }
  /* Front */
  .card-front {
    top: 42px;
    background: var(--card-light);
  }
  .name-marker {
    position: absolute;
    left: 0;
    top: 44px;
    width: 26px;
    height: 44px;
    background: var(--brand-red);
  }
  .person-name {
    position: absolute;
    left: 46px;
    top: 42px;
    font-weight: 800;
    font-size: 30px;
    letter-spacing: 1px;
    color: var(--brand-red);
    text-transform: uppercase;
  }
  .person-title {
    position: absolute;
    left: 46px;
    top: 80px;
    font-weight: 300;
    font-size: 20px;
    color: var(--ink-soft);
  }
  .address {
    position: absolute;
    left: 46px;
    top: 142px;
    font-weight: 400;
    font-size: 19px;
    line-height: 1.35;
    color: var(--ink);
  }
  .contact-list {
    position: absolute;
    left: 46px;
    top: 222px;
    list-style: none;
  }
  .contact-item {
    display: flex;
    align-items: center;
    gap: 10px;
    font-size: 18px;
    line-height: 30px;
    color: var(--ink);
  }
  .contact-icon {
    width: 16px;
    height: 16px;
    flex: none;
  }
  .front-brand {
    position: absolute;
    right: 44px;
    top: 150px;
    width: 250px;
    display: flex;
    flex-direction: column;
    align-items: center;
    gap: 18px;
  }
  .brand-square {
    width: 96px;
    height: 96px;
    background: var(--brand-red);
  }
  .brand-name {
    font-weight: 600;
    font-size: 22px;
    line-height: 1.25;
    letter-spacing: 2px;
    color: var(--brand-red);
    text-transform: uppercase;
    text-align: center;
  }
  /* Back */
  .card-back {
    top: 470px;
    background: var(--card-dark);
  }
  .back-pattern {
    position: absolute;
    inset: 0;
    background: linear-gradient(135deg, var(--pattern-b) 0%, var(--pattern-a) 45%, #55555a 70%, var(--pattern-b) 100%);
    opacity: 0.55;
  }
  .back-brand {
    position: absolute;
    left: 54px;
    bottom: 58px;
    display: flex;
    align-items: center;
    gap: 16px;
  }
  .back-brand .brand-square {
    width: 44px;
    height: 44px;
  }
  .back-brand .brand-name {
    font-size: 24px;
    text-align: left;
  }
</style>
</head>
<body>
<main class="canvas">

  <section class="card card-front" aria-label="Business card front">
    <span class="name-marker"></span>
    <h1 class="person-name">Daniel Reyes</h1>
    <p class="person-title">CEO/Founder</p>
    <p class="address">417 Canyon Ridge Drive<br>Provo, UT 84604</p>
    <ul class="contact-list">
      <li class="contact-item">
        <svg class="contact-icon" viewBox="0 0 16 16" aria-hidden="true"><path fill="#861812" d="M3.5 1.5l2.5 0 1 3.5-1.8 1.2a8 8 0 0 0 4.6 4.6L11 9l3.5 1v2.5c0 1-1 2-2 2A11 11 0 0 1 1.5 3.5c0-1 1-2 2-2z"/></svg>
        <span>801-555-0147</span>
      </li>
      <li class="contact-item">
        <svg class="contact-icon" viewBox="0 0 16 16" aria-hidden="true"><rect x="4" y="1" width="8" height="14" rx="1.5" fill="none" stroke="#861812" stroke-width="1.6"/><circle cx="8" cy="12.3" r="0.9" fill="#861812"/></svg>
        <span>385-555-0192</span>
      </li>
      <li class="contact-item">
        <svg class="contact-icon" viewBox="0 0 16 16" aria-hidden="true"><rect x="1" y="3" width="14" height="10" rx="1" fill="#861812"/><path d="M1.5 3.8L8 8.8l6.5-5" fill="none" stroke="#fff" stroke-width="1.3"/></svg>
        <span>info@halvorseneng.com</span>
      </li>
      <li class="contact-item">
        <svg class="contact-icon" viewBox="0 0 16 16" aria-hidden="true"><circle cx="8" cy="8" r="6.5" fill="none" stroke="#861812" stroke-width="1.5"/><ellipse cx="8" cy="8" rx="2.8" ry="6.5" fill="none" stroke="#861812" stroke-width="1.2"/><path d="M1.5 8h13" stroke="#861812" stroke-width="1.2"/></svg>
        <span>www.halvorseneng.com</span>
      </li>
    </ul>
    <div class="front-brand">
      <span class="brand-square"></span>
      <p class="brand-name">Halvorsen<br>Engineering</p>
    </div>
  </section>

  <section class="card card-back" aria-label="Business card back">
    <div class="back-pattern" role="img" aria-label="Repeating tonal pattern of the company emblem in dark and silver greys"></div>
    <div class="back-brand">
      <span class="brand-square"></span>
      <p class="brand-name">Halvorsen Engineering</p>
    </div>
  </section>

</main>
</body>
</html>
```